IT Company looking to market towards Dental Offices

I am looking for a full-color design. Using my existing logo. Must have High Res stock photos. The brochure needs to be full page edge to edge design single fold pamphlet style. Content provided. Please see the website in attached Word Doc for more content.

```html
<!DOCTYPE html>
<html lang="en">
<head>
<meta charset="utf-8">
<title>Chairside Tech – Dental IT Brochure</title>
<link href="https://fonts.googleapis.com/css2?family=Source+Sans+3:ital,wght@0,400;0,600;0,700;1,700&display=swap" rel="stylesheet">
<style>
:root{
  --bg:#d5d6d8;
  --navy:#0c2a6e;
  --blue:#1650b0;
  --bright:#2a6ad0;
  --ink:#333a48;
  --paper:#ffffff;
  --mist:#eef1f6;
  --silver:#c9ced8;
}
*{box-sizing:border-box;margin:0;padding:0}
html,body{width:937px;height:1200px;overflow:hidden;background:var(--bg);font-family:"Source Sans 3",Arial,sans-serif;color:var(--ink)}
.spread{position:absolute;left:92px;width:758px;height:490px;box-shadow:0 6px 8px rgba(0,0,0,.18)}
.spread--outer{top:76px}
.spread--inner{top:626px}
.page{position:absolute;top:0;width:379px;height:490px;overflow:hidden;background:var(--paper)}
.page--left{left:0}
.page--right{left:379px}
.abs{position:absolute}
.photo{position:absolute}
.body-copy{font-size:9px;line-height:1.32;color:var(--ink)}
.body-copy p+p{margin-top:9px}
.body-copy strong{color:var(--navy);font-style:italic}
.brand{font-weight:700;font-size:21px;letter-spacing:.3px;display:flex;align-items:center;gap:7px}
.brand__dot{width:14px;height:14px;border-radius:50%;background:currentColor}
.contact{color:#fff;font-size:11px;font-weight:600}
.contact li{list-style:none;display:flex;align-items:center;gap:9px;height:21px}
.contact svg{width:13px;height:13px}
.pill{background:var(--blue);color:#fff;border-radius:14px;font-size:14px;font-weight:600;letter-spacing:1px;display:flex;align-items:center;justify-content:center;gap:6px}
.tagline{color:var(--navy);font-style:italic;font-weight:700;font-size:10px;text-align:center;line-height:1.4;text-transform:uppercase}
.about{color:#fff;font-size:8.4px;line-height:1.3}
.about p+p{margin-top:9px}
.about__head{display:flex;align-items:center;gap:10px;font-weight:700;font-style:italic;font-size:11px}
.section{position:absolute;left:20px;width:350px;display:flex;gap:22px;z-index:2}
.section__icon{width:40px;height:40px;border-radius:50%;background:radial-gradient(circle at 40% 35%,var(--bright),var(--navy));box-shadow:0 3px 4px rgba(0,0,0,.25);flex:none;display:flex;align-items:center;justify-content:center}
.section__title{color:var(--navy);font-weight:700;font-style:italic;font-size:9px;line-height:11px}
.section ul{list-style:none;font-size:7.8px;line-height:12.3px;columns:2;column-gap:14px;width:280px}
.section ul.single{columns:1;line-height:11.1px;width:180px}
.section li::before{content:"• "}
.heading{color:var(--navy);font-style:italic;font-weight:700;font-size:11.5px;text-align:center}
.steps{border:1px solid var(--blue);border-radius:3px;background:#fff}
.steps__head{background:var(--blue);color:#fff;font-size:9.5px;text-align:center;height:23px;line-height:23px}
.steps ol{list-style:none;padding:10px 14px;font-size:8.6px;line-height:20px}
.steps b{color:var(--blue);margin-right:6px}
.note{font-size:8.6px;text-align:center;line-height:1.3}
.call{color:#fff;font-weight:600;font-size:14px;letter-spacing:1.3px;display:flex;align-items:center;gap:6px}
</style>
</head>
<body>

<!-- Outer spread -->
<section class="spread spread--outer">
  <div class="page page--left">
    <div class="photo" style="left:0;top:0;width:379px;height:150px;background:linear-gradient(120deg,#dfe6ee,#9fb7d6 55%,#4a73b2)" role="img" aria-label="Dentist and assistant treating a patient in the chair"></div>
    <div class="abs body-copy" style="left:20px;top:174px;width:345px">
      <p>Offsite backups for your practice management software made easy and automated. We know how to configure your Dental software to have successful backups every night and be secure, compliant, and verified. Our fully encrypted, enterprise-class offsite backup and recovery solution provides the ultimate protection.</p>
      <p>Get started today at <strong>www.toothsafe-backup.com</strong></p>
      <p>We don’t charge anything until we have confirmation that your Data has been successfully backed up on our encrypted servers.</p>
    </div>
    <svg class="abs" style="left:0;top:270px" width="379" height="220" viewBox="0 0 379 220">
      <defs><linearGradient id="lb" x1="0" y1="0" x2="1" y2="1"><stop offset="0" stop-color="#2a6ad0"/><stop offset="1" stop-color="#0c2a6e"/></linearGradient></defs>
      <path d="M0 0 C70 110 220 160 379 168 L379 220 L0 220Z" fill="url(#lb)"/>
      <path d="M0 -2 C70 104 220 152 379 160" fill="none" stroke="#fff" stroke-width="7"/>
      <path d="M0 -8 C70 98 220 146 379 154" fill="none" stroke="#1650b0" stroke-width="2"/>
    </svg>
    <div class="abs brand" style="left:190px;top:324px;color:var(--navy)"><span class="brand__dot"></span>Chairside Tech</div>
    <ul class="abs contact" style="left:20px;top:408px">
      <li><svg viewBox="0 0 16 16"><circle cx="8" cy="8" r="7" fill="none" stroke="#fff" stroke-width="1.3"/><path d="M5 4.5l1.5-.5 1 2-1 .8c.5 1.2 1.3 2 2.5 2.5l.8-1 2 1-.5 1.5C8 11 5 8 5 4.5Z" fill="#fff"/></svg>555-014-2290</li>
      <li><svg viewBox="0 0 16 16" fill="none" stroke="#fff" stroke-width="1.2"><circle cx="8" cy="8" r="7"/><ellipse cx="8" cy="8" rx="3" ry="7"/><path d="M1 8h14"/></svg>www.chairsidetech.com</li>
      <li><svg viewBox="0 0 16 16"><circle cx="8" cy="8" r="8" fill="#fff"/><path d="M8 3.5l4.5 4h-1.3v4H9.2V9H6.8v2.5H4.8v-4H3.5Z" fill="#1650b0"/></svg>48 Harbor Lane, Riverton, OR 97000</li>
    </ul>
  </div>

  <div class="page page--right">
    <svg class="abs" style="left:0;top:0" width="379" height="160" viewBox="0 0 379 160">
      <defs><linearGradient id="rt" x1="0" y1="0" x2="1" y2="0"><stop offset="0" stop-color="#1650b0"/><stop offset="1" stop-color="#0c2a6e"/></linearGradient></defs>
      <rect width="379" height="160" fill="url(#rt)"/>
    </svg>
    <div class="photo" style="left:0;top:92px;width:379px;height:335px;background:linear-gradient(160deg,#d9dde3,#a9b3c1 45%,#5d86c4 70%,#8d949e)" role="img" aria-label="Modern dental operatory with blue treatment chairs"></div>
    <svg class="abs" style="left:0;top:80px" width="379" height="50" viewBox="0 0 379 50">
      <path d="M0 50 C80 10 240 0 379 30 L379 0 L0 0Z" fill="#1650b0"/>
      <path d="M0 48 C80 8 240 -2 379 28" fill="none" stroke="#fff" stroke-width="6"/>
      <path d="M0 54 C80 14 240 4 379 34" fill="none" stroke="#c9ced8" stroke-width="4"/>
    </svg>
    <div class="abs brand" style="left:24px;top:28px;color:#fff;font-size:24px"><span class="brand__dot"></span>Chairside Tech</div>
    <div class="abs" style="left:0;top:424px;width:379px;height:66px;background:linear-gradient(#fff,var(--mist))"></div>
    <div class="abs pill" style="left:73px;top:408px;width:232px;height:30px">
      <svg width="14" height="14" viewBox="0 0 16 16"><circle cx="8" cy="8" r="7" fill="none" stroke="#fff" stroke-width="1.3"/><path d="M5 4.5l1.5-.5 1 2-1 .8c.5 1.2 1.3 2 2.5 2.5l.8-1 2 1-.5 1.5C8 11 5 8 5 4.5Z" fill="#fff"/></svg>555-014-2290
    </div>
    <p class="abs tagline" style="left:10px;top:447px;width:359px">Offsite backups for your practice management software<br>made easy and automated</p>
  </div>
</section>

<!-- Inner spread -->
<section class="spread spread--inner">
  <div class="page page--left" style="background:linear-gradient(#fff 40%,#e8edf5)">
    <div class="abs" style="left:0;top:0;width:379px;height:182px;background:linear-gradient(120deg,var(--navy),var(--blue))"></div>
    <div class="abs about" style="left:20px;top:18px;width:345px">
      <div class="about__head" style="margin-bottom:16px"><span class="brand__dot" style="width:24px;height:24px;background:#fff"></span>ABOUT US</div>
      <p>Chairside Tech offers a proven expertise in Dental Practices. We have trained engineers that specialize in Dental practice management solutions. We can handle supporting your Practice Management Software to installing IOCs, Remote &amp; Sensors, Pano’s, X-rays, scanners, pen pads, and more.</p>
      <p>Being familiar with Digital technology and how your practice runs we are able to predict and plan for your growth by providing the correct configurations the first time and implementing the proper storage solutions you will require.<br>We know Dental!</p>
    </div>

    <div class="section" style="top:200px">
      <div class="section__icon"><svg width="18" height="18" viewBox="0 0 18 18" fill="none" stroke="#fff" stroke-width="1.4"><rect x="4" y="4" width="10" height="10"/><path d="M7 1v3M11 1v3M7 14v3M11 14v3M1 7h3M1 11h3M14 7h3M14 11h3"/></svg></div>
      <div><div class="section__title">HARDWARE SALES</div>
        <ul><li>Servers</li><li>Workstations</li><li>Firewalls</li><li>Routers</li><li>Switches</li><li>TVs &amp; Monitors</li><li>Wireless Equipment</li><li>Custom Check-in Workstations</li></ul></div>
    </div>
    <div class="section" style="top:275px">
      <div class="section__icon"><svg width="18" height="18" viewBox="0 0 18 18" fill="none" stroke="#fff" stroke-width="1.6"><circle cx="9" cy="9" r="3"/><circle cx="9" cy="9" r="6.5" stroke-dasharray="2.5 2"/></svg></div>
      <div><div class="section__title">INFRASTRUCTURE</div>
        <ul><li>Data &amp; Voice Cable</li><li>HDMI &amp; COAX Video Cable</li><li>TV &amp; Dual Monitor Installation</li><li>Mounting Hardware</li><li>Wireless Installation</li><li>Office Sound Solutions</li><li>Custom Dental Cable</li><li>Video Surveillance</li></ul></div>
    </div>
    <div class="section" style="top:348px">
      <div class="section__icon"><svg width="18" height="18" viewBox="0 0 18 18" fill="none" stroke="#fff" stroke-width="1.4"><rect x="2" y="3" width="14" height="9" rx="1"/><path d="M6 15h6M9 12v3"/></svg></div>
      <div><div class="section__title">SOLUTIONS</div>
        <ul class="single"><li>Flat Rate Monthly Support</li><li>Secure Backups with our ToothSafe Backup</li><li>Secure Encrypted Emails &amp; X-Rays</li><li>Practice Management Software Experts</li><li>HIPAA Compliance</li><li>Anti-Virus, Anti-Malware and Cyber Security</li><li>Data Recovery</li><li>Cloud Office Suites</li><li>Phone VOIP &amp; SIP Trunks</li></ul></div>
    </div>
    <div class="photo" style="left:258px;top:360px;width:108px;height:88px;background:linear-gradient(135deg,#4a4f58,#16181c);border-radius:4px" role="img" aria-label="Desktop computer with monitor, keyboard and mouse"></div>
    <svg class="abs" style="left:0;top:455px" width="379" height="35" viewBox="0 0 379 35">
      <path d="M0 9 C120 10 260 8 379 5 L379 35 L0 35Z" fill="#0c2a6e"/>
      <path d="M0 8 C120 9 260 7 379 4" fill="none" stroke="#fff" stroke-width="2"/>
    </svg>
  </div>

  <div class="page page--right" style="background:linear-gradient(#fff 60%,var(--mist))">
    <div class="photo" style="left:0;top:0;width:379px;height:180px;background:linear-gradient(150deg,#eef0f3,#c5ccd6 50%,#7b8593)" role="img" aria-label="Bright dental treatment room with chair and wall-mounted monitors"></div>
    <svg class="abs" style="left:0;top:150px" width="379" height="50" viewBox="0 0 379 50">
      <path d="M0 40 C120 36 260 20 379 0 L379 50 L0 50Z" fill="#fff"/>
      <path d="M0 38 C120 34 260 18 379 -2" fill="none" stroke="#1650b0" stroke-width="3"/>
    </svg>
    <p class="abs heading" style="left:0;top:212px;width:379px">READY TO MAKE YOUR TECHNOLOGY WORK?</p>
    <div class="abs steps" style="left:19px;top:231px;width:340px;height:97px">
      <div class="steps__head">How To Achieve Technology Bliss for Your Practice</div>
      <ol><li><b>1.</b>Schedule a FREE Network &amp; Technology Evaluation</li><li><b>2.</b>Receive your Flat Rate Price and Technology Quote</li><li><b>3.</b>Sit back and let Chairside Tech take care of everything</li></ol>
    </div>
    <div class="abs note" style="left:30px;top:338px;width:320px">
      <p>Don’t let Technology Departments, Hardware Vendors and Practice Management vendors Point Fingers at each other.</p>
      <p style="margin-top:10px">We collaborate everything and everyone for you, make one call to us and let us handle your technology.</p>
    </div>
    <svg class="abs" style="left:0;top:400px" width="379" height="90" viewBox="0 0 379 90">
      <defs><linearGradient id="rb" x1="0" y1="0" x2="1" y2="0"><stop offset="0" stop-color="#0c2a6e"/><stop offset="1" stop-color="#1650b0"/></linearGradient></defs>
      <path d="M0 60 C140 56 270 30 379 0 L379 90 L0 90Z" fill="url(#rb)"/>
      <path d="M0 54 C140 48 270 22 379 -6" fill="none" stroke="#c9ced8" stroke-width="4"/>
    </svg>
    <div class="abs call" style="right:20px;top:460px">CALL US NOW!
      <svg width="15" height="15" viewBox="0 0 16 16"><circle cx="8" cy="8" r="7" fill="none" stroke="#fff" stroke-width="1.3"/><path d="M5 4.5l1.5-.5 1 2-1 .8c.5 1.2 1.3 2 2.5 2.5l.8-1 2 1-.5 1.5C8 11 5 8 5 4.5Z" fill="#fff"/></svg>555-014-2290</div>
  </div>
</section>

</body>
</html>
```